Hi Designers,

I will need 4 web pages designed. The web page looks like an App (if you click on the logo, or the icon on an iPad, it will take you to the website), but it is still a webpage.

Please check the attachment on this brief to understand what specific pages I need to be designed.

A .PSD (straight-up PhotoShop image) as final deliverable is fine, as long as you give us the exact “web color numbers”.

The design is for desktop and iPad but in a single unified web application, NOT separate web app and (native) iPad app.

Details:

Brightwell Ledger Advisory Group is developing a browser-based application for use on any mobile device or desktop. The app will be used by corporations to communicate with their employees regarding legal, regulatory and company requirements for conducting business. The app is known as “Harbor Rulebook Hub.” When the user clicks on the icon for Harbor Rulebook Hub, they will enter a site full of information that a company deems necessary for the employee to do his/her job. There are several content sections within the site, including a login page, training, policies, forms, news feeds and blogs.

The application has been built using Microsoft .NET, and fully supports CSS-type skinning; it uses traditional page layouts. We are seeking a product logo concept (image), a master application/desktop icon (image), as well as a full color scheme/theme/skin design for all areas of the application (header area, body text, menu bar, etc.) in the form of a CSS. The look should be clean, crisp and professional; nothing cartoony or whimsical. It should be easy to read and “airy”.

We have sketched prototypes for the basic application page layout that we can send as a next step of the process.
Updates

Screen shots have been uploaded to this project.  Please use them to guide your design.

Dear designers,

I apologize for the delay in providing feedback. My partners and I will provide feedback in a few days. Thank you for your patience.

Industry/Entity Type

Business

Font styles to use
Other font styles liked:
• see font on screen shots when uploaded

```html
<!DOCTYPE html>
<html lang="en">
<head>
<meta charset="utf-8">
<title>Harbor Rulebook Hub</title>
<link href="https://fonts.googleapis.com/css2?family=Source+Sans+3:wght@400;600&display=swap" rel="stylesheet">
<style>
:root{
  --blue:#1d5aa0;
  --blue-dark:#174a87;
  --link:#1f6fc4;
  --orange:#d98a00;
  --green:#5ba21f;
  --green-dark:#4a8a16;
  --steel:#5f8fc7;
  --text:#555;
  --text-dark:#444;
  --line:#d8d8d8;
  --card:#f4f4f4;
  --card-border:#dcdcdc;
  --footer:#ececec;
}
*{box-sizing:border-box;margin:0;padding:0}
html,body{width:1070px;height:1200px;overflow:hidden;background:#fff}
body{font-family:"Source Sans 3",Arial,sans-serif;color:var(--text)}
.stage{position:absolute;left:0;top:0;width:1150px;height:1290px;transform:scale(.9304);transform-origin:0 0}
.abs{position:absolute}

/* header */
.brand{left:97px;top:20px;display:flex;align-items:center;gap:14px}
.brand-mark{width:40px;height:40px;border-radius:50%;background:var(--blue)}
.brand-name{color:var(--blue);font-size:23px;line-height:29px;font-weight:400;letter-spacing:1px;text-transform:uppercase}
.main-nav{left:529px;top:20px;height:30px;display:flex;border:1px solid #ccc;border-radius:3px;background:linear-gradient(#fafafa,#e9e9e9)}
.main-nav a{display:flex;align-items:center;gap:6px;padding:0 13px;font-size:14px;color:#444;text-decoration:none;border-right:1px solid #d0d0d0}
.main-nav a:last-child{border-right:0}
.main-nav a.active{color:var(--blue);background:#f2f2f2}
.search{left:872px;top:20px;width:182px;height:31px;border:1px solid #ccc;background:#fff;display:flex;align-items:center;justify-content:space-between;padding:0 9px;font-size:13px;color:#999}
.points{left:779px;top:69px;width:76px;height:31px;border-radius:3px;background:linear-gradient(#3d84d6,#1c5db0);border:1px solid #154e96;display:flex;align-items:center;gap:10px;padding-left:10px;color:#fff;font-weight:600;font-size:16px}
.points .coin{width:16px;height:16px;border-radius:50%;background:#f5b400;color:#5a3c00;font-size:10px;display:flex;align-items:center;justify-content:center}
.user{left:872px;top:69px;width:182px;height:31px;border:1px solid #ccc;background:linear-gradient(#fff,#f0f0f0);display:flex;align-items:center;padding:0 2px;font-size:13px;color:#666}
.user .avatar{width:26px;height:26px;background:#8a7a70;margin-right:12px}
.user .caret{margin-left:auto;margin-right:10px;border:6px solid transparent;border-top:6px solid #999;margin-top:6px}

/* welcome */
.welcome{left:95px;top:130px;width:960px;height:44px;border-radius:2px;background:linear-gradient(#6a6a6a,#3e3e3e);color:#fff;font-size:16px;padding:12px 19px}
.intro-photo{left:97px;top:193px;width:228px;height:123px;background:linear-gradient(120deg,#8ab0d6,#e0e4ea 45%,#5f7fa3 70%,#c34a5e)}
.intro-text{left:341px;top:191px;width:714px;font-size:14px;line-height:24px;color:var(--text)}
.intro-text p+p{margin-top:8px}

.rule{left:96px;width:959px;height:1px;background:var(--line)}

/* feature columns */
.col{width:310px}
.col-head{height:38px;border-radius:2px;display:flex;align-items:center;padding:0 12px 0 18px;color:#fff;font-size:17px;gap:12px}
.col-head .go{margin-left:auto;width:18px;height:18px;border-radius:50%;background:rgba(255,255,255,.85);display:flex;align-items:center;justify-content:center}
.head-news{background:linear-gradient(#2a6ab8,#184e92)}
.head-blog{background:linear-gradient(#6cbc28,var(--green-dark))}
.head-forms{background:linear-gradient(#7ea7d8,#4f80bd)}
.card{margin-top:8px;height:116px;background:var(--card);border:1px solid var(--card-border);padding:15px 19px;font-size:14px;line-height:20px;color:var(--text-dark)}
.card+.card{margin-top:4px}
.card .date{color:var(--orange);margin-top:4px}
.card .source{color:var(--link);font-size:13px;margin-top:2px}
.card.with-thumb{display:flex;gap:13px;padding:15px 10px 15px 15px}
.thumb{flex:none;width:66px;height:80px;border:1px solid #ccc;border-radius:3px}
.t1{background:linear-gradient(#eef2f5,#c7d0d8 60%,#9aa6b2)}
.t2{background:linear-gradient(#dff3f8,#7fd0e0 60%,#4aa86a)}
.t3{background:linear-gradient(#fff,#e8e8e8 70%,#c9a27c)}

/* info boxes */
.sect-title{display:flex;align-items:center;gap:12px;color:var(--blue);font-size:20px;height:32px}
.box{margin-top:4px;height:159px;background:var(--card);border:1px solid var(--card-border);padding:16px 17px;font-size:13px;line-height:20px;color:var(--text-dark)}
.box .q{color:var(--link);font-size:14px;line-height:18px;margin-bottom:6px}
.box .date{color:var(--orange);font-size:14px;margin-top:4px}
.report{display:flex;padding:0}
.report .half{flex:1;padding:24px 0 0 35px;font-size:13px;line-height:30px}
.report .half+.half{border-left:1px solid var(--card-border)}
.report dt{display:inline-block;width:40px}
.report dd{display:inline;color:var(--link);font-size:14px}

/* links */
.links-title{left:112px;top:1056px;display:flex;align-items:center;gap:12px;color:var(--blue);font-size:20px}
.link-list{top:1099px;list-style:none;font-size:14px;color:#444;line-height:28px}
.link-list li::before{content:"»";margin-right:8px;color:#555}

/* footer */
.footer{left:0;top:1202px;width:1150px;height:88px;background:var(--footer)}
.footer-nav{left:96px;top:1220px;font-size:14px;color:#555;display:flex;gap:10px}
.footer-nav span.sep{color:#aaa}
.copyright{left:96px;top:1252px;font-size:14px;color:#555;word-spacing:2px}
.social{top:1234px;width:22px;height:22px;border-radius:3px}
</style>
</head>
<body>
<div class="stage">

  <header>
    <div class="abs brand">
      <span class="brand-mark"></span>
      <span class="brand-name">Harbor<br>Rulebook<br>Hub</span>
    </div>
    <nav class="abs main-nav">
      <a class="active" href="#"><svg width="16" height="14" viewBox="0 0 16 14"><path d="M8 1 1 7h2v6h4V9h2v4h4V7h2z" fill="#3b6fb0"/></svg>Home</a>
      <a href="#"><svg width="14" height="11" viewBox="0 0 14 11" fill="#555"><rect width="2" height="2"/><rect x="4" width="10" height="2"/><rect y="4.5" width="2" height="2"/><rect x="4" y="4.5" width="10" height="2"/><rect y="9" width="2" height="2"/><rect x="4" y="9" width="10" height="2"/></svg>Menu</a>
      <a href="#"><svg width="10" height="16" viewBox="0 0 10 16" fill="#555"><circle cx="5" cy="5" r="4.5"/><path d="M2 8l-1 8 4-2 4 2-1-8z"/></svg>Game</a>
      <a href="#"><svg width="14" height="14" viewBox="0 0 14 14"><circle cx="7" cy="7" r="6.5" fill="#555"/><path d="M7 7V.5A6.5 6.5 0 0 1 13.5 7z" fill="#fff"/></svg>Pro 360</a>
    </nav>
    <div class="abs search">Search<svg width="15" height="15" viewBox="0 0 15 15"><circle cx="6" cy="6" r="4.5" fill="none" stroke="#222" stroke-width="2"/><path d="M9 9l5 5" stroke="#222" stroke-width="3"/></svg></div>
    <div class="abs points"><span class="coin">1</span>427</div>
    <div class="abs user"><span class="avatar" role="img" aria-label="User avatar"></span>Dale Orton<span class="caret"></span></div>
  </header>

  <div class="abs welcome">Welcome to the Harbor Rulebook Hub</div>
  <div class="abs intro-photo" role="img" aria-label="Lab technician working with sample tubes"></div>
  <div class="abs intro-text">
    <p>Donec tincidunt, orci sit amet lobortis luctus, mi tortor posuere erat, sit amet ullamcorper lacus massa ut nibh. In hac habitasse platea dictumst. Quisque vestibulum augue id eros mattis molestie. Nulla facilisi. Aliquam et diam lectus. Class aptent taciti sociosqu ad litora torquent per conubia nostra, per inceptos himenaeos.</p>
    <p>Donec aliquam pretium condimentum. Aenean consectetur enim eget eros iaculis, vitae accumsan massa gravida. Donec et urna tellus. Nulla vehicula orci dui, nec feugiat odio tempus a. Sed venenatis augue sit amet massa scelerisque hendrerit.</p>
  </div>

  <div class="abs rule" style="top:354px"></div>

  <section class="abs col" style="left:96px;top:360px">
    <div class="col-head head-news">
      <svg width="24" height="20" viewBox="0 0 24 20"><rect x="1" y="1" width="22" height="18" fill="none" stroke="#fff" stroke-width="2"/><rect x="4" y="5" width="7" height="6" fill="#fff"/><path d="M13 6h7M13 10h7M4 14h16" stroke="#fff" stroke-width="2"/></svg>
      Compliance News<span class="go"><svg width="8" height="8" viewBox="0 0 8 8"><path d="M2 1l3 3-3 3" stroke="#1d5aa0" stroke-width="2" fill="none"/></svg></span>
    </div>
    <article class="card">Nivamus id magna sit amet magna molestie imperdiet quis a nulla.<div class="date">Nov - 16 - 2013</div><div class="source">Reg Wire : Pharma Sector Daily</div></article>
    <article class="card">Nivamus id magna sit amet magna molestie imperdiet quis a nulla.<div class="date">Nov - 16 - 2013</div><div class="source">Reg Wire : Pharma Sector Daily</div></article>
    <article class="card">Nivamus id magna sit amet magna molestie imperdiet quis a nulla.<div class="date">Nov - 16 - 2013</div><div class="source">Reg Wire : Pharma Sector Daily</div></article>
  </section>

  <section class="abs col" style="left:421px;top:360px">
    <div class="col-head head-blog">
      <svg width="24" height="20" viewBox="0 0 24 20" fill="#fff"><path d="M2 7h4l12-6v18L6 13H2z"/><rect x="6" y="13" width="4" height="6"/></svg>
      Compliance Blog<span class="go"><svg width="8" height="8" viewBox="0 0 8 8"><path d="M2 1l3 3-3 3" stroke="#4a8a16" stroke-width="2" fill="none"/></svg></span>
    </div>
    <article class="card with-thumb"><div class="thumb t1" role="img" aria-label="Test tubes in a rack"></div><div>Nivamus id magna sit amet magna molestie imperdiet quis a nulla. Aenean ullamcorper porttito.<div class="date">Nov - 16 - 2013</div></div></article>
    <article class="card with-thumb"><div class="thumb t2" role="img" aria-label="Beaker with liquid"></div><div>Nivamus id magna sit amet magna molestie imperdiet quis a nulla. Aenean ullamcorper porttito.<div class="date">Nov - 16 - 2013</div></div></article>
    <article class="card with-thumb"><div class="thumb t3" role="img" aria-label="Capsules above an open hand"></div><div>Nivamus id magna sit amet magna molestie imperdiet quis a nulla. Aenean ullamcorper porttito.<div class="date">Nov - 16 - 2013</div></div></article>
  </section>

  <section class="abs col" style="left:745px;top:360px">
    <div class="col-head head-forms">
      <svg width="26" height="20" viewBox="0 0 26 20" fill="#fff"><rect x="6" y="1" width="14" height="10"/><path d="M1 11h7l2 3h6l2-3h7v8H1z"/></svg>
      Forms<span class="go"><svg width="8" height="8" viewBox="0 0 8 8"><path d="M2 1l3 3-3 3" stroke="#4f80bd" stroke-width="2" fill="none"/></svg></span>
    </div>
    <article class="card">Nivamus id magna sit amet magna molestie imperdiet quis a nulla.<div class="date">Nov - 16 - 2013</div><div class="source">Reg Wire : Pharma Sector Daily</div></article>
    <article class="card">Nivamus id magna sit amet magna molestie imperdiet quis a nulla.<div class="date">Nov - 16 - 2013</div><div class="source">Reg Wire : Pharma Sector Daily</div></article>
    <article class="card">Nivamus id magna sit amet magna molestie imperdiet quis a nulla.<div class="date">Nov - 16 - 2013</div><div class="source">Reg Wire : Pharma Sector Daily</div></article>
  </section>

  <div class="abs rule" style="top:795px"></div>

  <section class="abs col" style="left:96px;top:809px">
    <h2 class="sect-title" style="font-weight:400"><svg width="27" height="27" viewBox="0 0 27 27"><circle cx="13.5" cy="13.5" r="13" fill="#1d5aa0"/><text x="13.5" y="20" font-size="18" font-weight="600" fill="#fff" text-anchor="middle" font-family="Arial,sans-serif">?</text></svg>FAQ’s</h2>
    <div class="box"><div class="q">Q : Donec tincidunt, orci sit amet lobortis luctus, mi tortor posuere erat?</div>Nivamus id magna sit amet magna molestie imperdiet quis a nulla. Nulla facilisi. Aliquam et diam lectus.<div class="date">Nov - 16 - 2013</div></div>
  </section>

  <section class="abs col" style="left:421px;top:809px">
    <h2 class="sect-title" style="font-weight:400"><svg width="22" height="26" viewBox="0 0 22 26"><path d="M1 1h14l6 6v18H1z" fill="#1d5aa0"/><path d="M5 10h12M5 14h12M5 18h12" stroke="#fff" stroke-width="1.6"/></svg>Document Library</h2>
    <div class="box"><div class="q">Donec tincidunt, orci sit amet lobortis luctus, mi tortor posuere erat?</div>Nivamus id magna sit amet magna molestie imperdiet quis a nulla. Nulla facilisi. Aliquam et diam lectus.<div class="date">Nov - 16 - 2013</div></div>
  </section>

  <section class="abs col" style="left:745px;top:809px">
    <h2 class="sect-title" style="font-weight:400"><svg width="28" height="28" viewBox="0 0 28 28"><rect x="2" y="3" width="24" height="15" fill="none" stroke="#1d5aa0" stroke-width="2"/><circle cx="10" cy="10" r="4" fill="#1d5aa0"/><path d="M16 8h7M16 12h7M14 18l-5 9M14 18l5 9" stroke="#1d5aa0" stroke-width="2"/></svg>Reports</h2>
    <div class="box report">
      <dl class="half"><dt>Player</dt>: <dd>Jon.K</dd><br><dt>Rank</dt>: <dd>4</dd><br><dt>Score</dt>: <dd>456</dd><br><dt>%</dt>: <dd>88%</dd></dl>
      <dl class="half"><dt>Player</dt>: <dd>Jon.K</dd><br><dt>Rank</dt>: <dd>4</dd><br><dt>Score</dt>: <dd>456</dd><br><dt>%</dt>: <dd>88%</dd></dl>
    </div>
  </section>

  <div class="abs rule" style="top:1034px"></div>

  <h2 class="abs links-title" style="font-weight:400"><svg width="26" height="26" viewBox="0 0 26 26" fill="none" stroke="#1d5aa0" stroke-width="2.5"><rect x="12" y="2" width="7" height="12" rx="3.5" transform="rotate(45 15.5 8)"/><rect x="7" y="12" width="7" height="12" rx="3.5" transform="rotate(45 10.5 18)"/></svg>Relevant Links</h2>
  <ul class="abs link-list" style="left:112px"><li>Class aptent taciti</li><li>Phasellus dapibus eros</li><li>Nulla eget</li></ul>
  <ul class="abs link-list" style="left:323px"><li>Donec tincidunt</li><li>Donec et urna tellus</li><li>Aenean consectetur</li></ul>
  <ul class="abs link-list" style="left:524px"><li>Quisque vestibulum</li><li>Quisque</li><li>Proin ultricies urna</li></ul>
  <ul class="abs link-list" style="left:725px"><li>Fusce vel</li><li>Aenean pretium risus</li><li>Mauris dictum</li></ul>
  <ul class="abs link-list" style="left:919px"><li>Curabitur sed</li><li>Morbi semper</li><li>Donec eget porta</li></ul>

  <footer>
    <div class="abs footer"></div>
    <nav class="abs footer-nav"><span>Home</span><span class="sep">|</span><span>Menu</span><span class="sep">|</span><span>Game</span><span class="sep">|</span><span>Pro 360</span></nav>
    <div class="abs copyright">Copyright © 2013 &nbsp;Harbor Rulebook Hub. &nbsp;All rights reserved.</div>
    <span class="abs social" style="left:1003px;background:#3d5d9c" role="img" aria-label="Social network link"></span>
    <span class="abs social" style="left:1032px;background:#45b0e3" role="img" aria-label="Social network link"></span>
  </footer>

</div>
</body>
</html>
```